Website design using a wordpress template I purchased

I have purchased a wordpress template called "Vantrel" from Plumora and would like to design a website using it for a financial services company. The site simply needs to be informational about the company and a blog. Nothing too involved. The company provides paymaster / escrow services for commodity transactions. I am working on the logo currently and will have it ready to provide shortly. I can provide the content for the informational portion of the site as well. I would like some quick tutoring regarding how to administer the blog portion of the site once built.

```html
<!DOCTYPE html>
<html lang="en">
<head>
<meta charset="utf-8">
<title>Financial Services – Home</title>
<link href="https://fonts.googleapis.com/css2?family=Roboto:wght@400;500;700;900&family=Lato:wght@400;700&display=swap" rel="stylesheet">
<style>
:root{
  --navy:#0f3b73;
  --navy-deep:#0b2a55;
  --yellow:#f0b90b;
  --ink:#1b1b1b;
  --body:#4a4a4a;
  --white:#ffffff;
  --blog-bg:#e6eaf1;
  --line:#f3de98;
}
*{margin:0;padding:0;box-sizing:border-box}
html,body{width:1200px;height:2380px;overflow:hidden;background:var(--white)}
body{font-family:'Lato',sans-serif;color:var(--ink)}
.page{position:relative;width:1200px;height:2380px;overflow:hidden}
.abs{position:absolute}
.icon-arrow{display:inline-block;vertical-align:middle}

/* Hero */
.hero{left:0;top:0;width:1200px;height:693px;background:radial-gradient(ellipse at 80% 40%,#2c5b8f 0%,#15355f 45%,#0b1f3d 100%)}
.header{left:75px;top:0;width:1050px;height:96px;background:var(--white);border-radius:0 0 20px 20px;display:flex;align-items:center;padding:0 33px 0 32px}
.brand{font-family:'Roboto',sans-serif;font-weight:700;font-size:27px;letter-spacing:1px;color:var(--ink)}
.nav{display:flex;gap:38px;margin-left:auto;margin-right:50px;font-size:16px;font-weight:400;color:var(--ink)}
.btn{display:inline-flex;align-items:center;gap:8px;height:45px;padding:0 18px;border-radius:23px;font-family:'Lato',sans-serif;font-size:16px;white-space:nowrap}
.btn-navy{background:var(--navy);color:var(--white)}
.btn-white{background:var(--white);color:var(--ink)}
.btn-yellow{background:var(--yellow);color:var(--white)}
.btn-outline{border:2px solid var(--yellow);color:var(--ink);background:transparent}
.hero-title{left:112px;top:272px;font-family:'Roboto',sans-serif;font-weight:700;font-size:49px;line-height:59px;letter-spacing:1px;color:var(--white)}
.hl{color:var(--yellow)}
.hero-cta{left:112px;top:477px}
.dots{left:570px;top:644px;display:flex;gap:6px}
.dots span{width:7px;height:7px;border-radius:50%;background:var(--white)}
.dots .on{background:var(--yellow)}

/* About */
.about-title{left:113px;top:790px;font-family:'Roboto',sans-serif;font-weight:700;font-size:38px;letter-spacing:1px}
.about-text{left:113px;top:858px;width:475px;font-size:13.6px;line-height:24.8px;color:var(--body)}
.about-text p+p{margin-top:24px}
.about-cta{left:112px;top:1160px}
.frame-line{left:672px;top:850px;width:438px;height:376px;border:2px solid var(--line);border-radius:0 40px 0 0;border-top-left-radius:0}
.frame-photo{left:617px;top:797px;width:471px;height:404px;background:var(--white);border-radius:0 40px 0 40px;box-shadow:0 0 8px rgba(0,0,0,.12);padding:6px}
.frame-photo div{width:100%;height:100%;border-radius:0 36px 0 36px;background:linear-gradient(135deg,#d9d4cc 0%,#9aa3ad 45%,#4b3a2c 100%)}

/* Blog */
.blog{left:0;top:1310px;width:1200px;height:776px;background:var(--blog-bg)}
.blog-title{left:0;top:1394px;width:1200px;text-align:center;font-family:'Roboto',sans-serif;font-weight:700;font-size:38px;letter-spacing:1px}
.card{top:1467px;width:307px;height:444px;background:var(--white);padding:5px}
.card-photo{width:297px;height:203px}
.date{position:absolute;left:28px;top:191px;height:36px;padding:0 15px 0 15px;border-radius:18px;background:var(--navy);color:var(--white);font-size:14px;display:flex;align-items:center;gap:14px}
.card-body{padding:48px 22px 0 23px}
.card h3{font-family:'Roboto',sans-serif;font-weight:400;font-size:18px;line-height:24px;color:#3a3a3a}
.card p{margin-top:14px;font-size:12px;line-height:19px;color:var(--body)}
.read{margin-top:16px;display:inline-flex;align-items:center;gap:6px;font-size:14px;font-weight:700;color:var(--navy);text-decoration:underline}
.slide-arrow{top:1678px}
.blog-btns{left:0;top:1950px;width:1200px;display:flex;justify-content:center;gap:23px}

/* Footer */
.footer{left:0;top:2086px;width:1200px;height:294px;background:linear-gradient(120deg,#16447f 0%,#113b72 50%,#1a4a86 100%)}
.footer-brand{left:0;top:2140px;width:1200px;text-align:center;font-family:'Roboto',sans-serif;font-weight:700;font-size:48px;letter-spacing:1px;color:var(--white)}
.social{left:0;top:2222px;width:1200px;display:flex;justify-content:center;gap:8px}
.social span{width:20px;height:20px;border-radius:50%;background:var(--white)}
.social .mid{background:var(--yellow)}
.footer-nav{left:0;top:2270px;width:1200px;display:flex;justify-content:center;gap:22px;font-size:14.5px;font-weight:700;color:var(--white)}
.copyright{left:0;top:2318px;width:1200px;text-align:center;font-size:11px;color:var(--white)}
</style>
</head>
<body>
<div class="page">

  <section class="abs hero" role="img" aria-label="Photo of a businessman's hands sheltering a glowing dollar sign against a blue bokeh background"></section>

  <header class="abs header">
    <div class="brand">COMPANY LOGO</div>
    <nav class="nav"><span>HOME</span><span>ABOUT US</span><span>SERVICES</span><span>BLOG</span><span>CONTACT US</span></nav>
    <span class="btn btn-navy">GET STARTED
      <svg class="icon-arrow" width="14" height="14" viewBox="0 0 14 14"><circle cx="7" cy="7" r="7" fill="#fff"/><path d="M3.5 7h6M7 4.5 9.5 7 7 9.5" stroke="#0f3b73" stroke-width="1.6" fill="none"/></svg></span>
  </header>

  <h1 class="abs hero-title"><span class="hl">LIVE</span> LIFE <span class="hl">TODAY</span>.<br>BE <span class="hl">CONFIDENT</span> ABOUT<br><span class="hl">TOMORROW</span>.</h1>
  <div class="abs hero-cta"><span class="btn btn-white">GET STARTED
    <svg class="icon-arrow" width="14" height="14" viewBox="0 0 14 14"><circle cx="7" cy="7" r="7" fill="#1b1b1b"/><path d="M3.5 7h6M7 4.5 9.5 7 7 9.5" stroke="#fff" stroke-width="1.6" fill="none"/></svg></span></div>
  <div class="abs dots"><span></span><span></span><span class="on"></span><span></span><span></span></div>

  <h2 class="abs about-title">ABOUT <span class="hl">THE COMPANY</span></h2>
  <div class="abs about-text">
    <p>Contrary to popular belief, Lorem Ipsum is not simply random text. It has roots in a piece of classical Latin literature from 45 BC, making it over 2000 years old. Harlan Pemberly, a Latin professor at Ashgrove-Linley College in Virginia, looked up one of the more obscure Latin words, consectetur, from a Lorem Ipsum passage, and going through the cites of the word in classical literature, discovered the undoubtable source.</p>
    <p>Contrary to popular belief, Lorem Ipsum is not simply random text. It has roots in a piece of classical Latin literature from 45 BC, making it over 2000 years old. Harlan Pemberly, a Latin professor at Ashgrove-Linley College in Virginia, looked up one of the more obscure Latin words</p>
  </div>
  <div class="abs about-cta"><span class="btn btn-navy" style="font-size:17px;padding:0 18px 0 19px">READ MORE
    <svg class="icon-arrow" width="14" height="14" viewBox="0 0 14 14"><circle cx="7" cy="7" r="7" fill="#fff"/><path d="M3.5 7h6M7 4.5 9.5 7 7 9.5" stroke="#0f3b73" stroke-width="1.6" fill="none"/></svg></span></div>
  <div class="abs frame-line"></div>
  <div class="abs frame-photo"><div role="img" aria-label="Photo of a team meeting around a table with laptops by a bright window"></div></div>

  <section class="abs blog"></section>
  <h2 class="abs blog-title">LATEST <span class="hl">BLOG</span></h2>

  <svg class="abs slide-arrow" style="left:60px" width="22" height="22" viewBox="0 0 22 22"><circle cx="11" cy="11" r="11" fill="#8a8f96"/><path d="M16 11H6M9.5 7.5 6 11l3.5 3.5" stroke="#fff" stroke-width="1.6" fill="none"/></svg>
  <svg class="abs slide-arrow" style="left:1118px" width="22" height="22" viewBox="0 0 22 22"><circle cx="11" cy="11" r="11" fill="#8a8f96"/><path d="M6 11h10M12.5 7.5 16 11l-3.5 3.5" stroke="#fff" stroke-width="1.6" fill="none"/></svg>

  <article class="abs card" style="left:120px">
    <div class="card-photo" role="img" aria-label="Photo of three colleagues talking in a bright lounge" style="background:linear-gradient(135deg,#e9ecef 0%,#aeb6c0 50%,#2c3440 100%)"></div>
    <div class="date"><svg width="17" height="17" viewBox="0 0 17 17"><rect x="1" y="2.5" width="15" height="13.5" rx="1.5" fill="none" stroke="#fff" stroke-width="1.4"/><path d="M1 6.5h15M5 1v3M12 1v3M4 9h2M7.5 9h2M11 9h2M4 12h2M7.5 12h2M11 12h2" stroke="#fff" stroke-width="1.3"/></svg>October 20, 2022</div>
    <div class="card-body">
      <h3>Contrary to popular belief, Lorem Ipsum is&nbsp; random text.</h3>
      <p>The standard chunk of Lorem Ipsum used since the 1500s is reproduced below for those interested. Sections 1.10.32 and 1.10.33 from "de Finibus Bonorum et Malorum</p>
      <span class="read">Read More <svg width="16" height="16" viewBox="0 0 14 14"><circle cx="7" cy="7" r="7" fill="#0f3b73"/><path d="M3.5 7h6M7 4.5 9.5 7 7 9.5" stroke="#fff" stroke-width="1.6" fill="none"/></svg></span>
    </div>
  </article>
  <article class="abs card" style="left:446px">
    <div class="card-photo" role="img" aria-label="Photo of hands reviewing charts on a tablet beside a laptop" style="background:linear-gradient(135deg,#f1f0ee 0%,#b9bfc6 50%,#5c6772 100%)"></div>
    <div class="date"><svg width="17" height="17" viewBox="0 0 17 17"><rect x="1" y="2.5" width="15" height="13.5" rx="1.5" fill="none" stroke="#fff" stroke-width="1.4"/><path d="M1 6.5h15M5 1v3M12 1v3M4 9h2M7.5 9h2M11 9h2M4 12h2M7.5 12h2M11 12h2" stroke="#fff" stroke-width="1.3"/></svg>October 20, 2022</div>
    <div class="card-body">
      <h3>Contrary to popular belief, Lorem Ipsum is&nbsp; random text.</h3>
      <p>The standard chunk of Lorem Ipsum used since the 1500s is reproduced below for those interested. Sections 1.10.32 and 1.10.33 from "de Finibus Bonorum et Malorum</p>
      <span class="read">Read More <svg width="16" height="16" viewBox="0 0 14 14"><circle cx="7" cy="7" r="7" fill="#0f3b73"/><path d="M3.5 7h6M7 4.5 9.5 7 7 9.5" stroke="#fff" stroke-width="1.6" fill="none"/></svg></span>
    </div>
  </article>
  <article class="abs card" style="left:772px">
    <div class="card-photo" role="img" aria-label="Photo of three coworkers discussing documents around a laptop" style="background:linear-gradient(135deg,#cfd3d6 0%,#7e8a93 50%,#3a2f35 100%)"></div>
    <div class="date"><svg width="17" height="17" viewBox="0 0 17 17"><rect x="1" y="2.5" width="15" height="13.5" rx="1.5" fill="none" stroke="#fff" stroke-width="1.4"/><path d="M1 6.5h15M5 1v3M12 1v3M4 9h2M7.5 9h2M11 9h2M4 12h2M7.5 12h2M11 12h2" stroke="#fff" stroke-width="1.3"/></svg>October 20, 2022</div>
    <div class="card-body">
      <h3>Contrary to popular belief, Lorem Ipsum is&nbsp; random text.</h3>
      <p>The standard chunk of Lorem Ipsum used since the 1500s is reproduced below for those interested. Sections 1.10.32 and 1.10.33 from "de Finibus Bonorum et Malorum</p>
      <span class="read">Read More <svg width="16" height="16" viewBox="0 0 14 14"><circle cx="7" cy="7" r="7" fill="#0f3b73"/><path d="M3.5 7h6M7 4.5 9.5 7 7 9.5" stroke="#fff" stroke-width="1.6" fill="none"/></svg></span>
    </div>
  </article>

  <div class="abs blog-btns">
    <span class="btn btn-yellow" style="width:150px;justify-content:center;gap:14px">VIEW MORE
      <svg width="14" height="14" viewBox="0 0 14 14"><circle cx="7" cy="7" r="7" fill="#fff"/><path d="M3.5 7h6M7 4.5 9.5 7 7 9.5" stroke="#f0b90b" stroke-width="1.6" fill="none"/></svg></span>
    <span class="btn btn-outline" style="width:149px;justify-content:center">GET STARTED
      <svg width="14" height="14" viewBox="0 0 14 14"><circle cx="7" cy="7" r="7" fill="#1b1b1b"/><path d="M3.5 7h6M7 4.5 9.5 7 7 9.5" stroke="#fff" stroke-width="1.6" fill="none"/></svg></span>
  </div>

  <footer class="abs footer" role="img" aria-label="Faint photo of a business team in a blue overlay"></footer>
  <div class="abs footer-brand">COMPANY LOGO</div>
  <div class="abs social"><span></span><span class="mid"></span><span></span></div>
  <nav class="abs footer-nav"><span>HOME</span><span>|</span><span>ABOUT US</span><span>|</span><span>SERVICES</span><span>|</span><span>LATEST BLOGS</span><span>|</span><span>CONTACT US</span><span>|</span><span>SITE MAP</span></nav>
  <div class="abs copyright">© 2022 Copyright company Name | All rights Reserved.</div>

</div>
</body>
</html>
```